Redesign Website Homepage Header

We are looking for a re-design of the header section of our website homepage. The style of the website, image assets and copy can all remain the same, but we want an alternative layout that matches the rest of the website. Full brief attached.

Reason: Project has been launched over a weekend so might have low response. Extending to cover more working week days.

```html
<!DOCTYPE html>
<html lang="en">
<head>
<meta charset="utf-8">
<title>Hosted Desktops for IT Resellers – Header Options</title>
<link rel="stylesheet" href="https://fonts.googleapis.com/css2?family=Montserrat:wght@500;600&display=swap">
<style>
  :root {
    --canvas: #ffffff;
    --ink: #0a0a0a;
    --white: #ffffff;
    --accent-red: #9e1518;
    --sky-light: #eef4fa;
    --sky-mid: #c9dbeb;
    --steel-blue: #7f9fc4;
    --navy: #2c4a7a;
  }
  * { margin: 0; padding: 0; box-sizing: border-box; }
  html, body {
    width: 1200px;
    height: 900px;
    overflow: hidden;
    background: var(--canvas);
    font-family: "Montserrat", sans-serif;
  }
  .board { position: relative; width: 1200px; height: 900px; }

  .header-option { position: absolute; left: 0; width: 1200px; }
  .header-option--one { top: 18px; height: 380px; }
  .header-option--two { top: 430px; height: 380px; }

  .backdrop-photo {
    position: absolute; inset: 0;
    background:
      radial-gradient(ellipse at 25% 40%, rgba(255,255,255,0.95), rgba(255,255,255,0) 60%),
      linear-gradient(180deg, var(--sky-mid) 0%, var(--sky-light) 55%, #e3e8ee 100%);
  }
  .portrait-photo {
    position: absolute; left: 750px; top: 0; width: 330px; height: 380px;
    background: linear-gradient(180deg, #d7e3ef 0%, var(--steel-blue) 55%, #c8b8b4 100%);
    opacity: 0.85;
  }
  .crowd-photo {
    position: absolute; left: 620px; top: 10px; width: 580px; height: 370px;
    background:
      radial-gradient(ellipse at 55% 45%, var(--navy) 0%, var(--steel-blue) 45%, rgba(201,219,235,0.6) 75%, rgba(255,255,255,0) 100%);
  }

  .headline { position: absolute; line-height: 1; }
  .headline__top, .headline__main { display: block; white-space: nowrap; }
  .headline__tag {
    display: inline-block; background: var(--accent-red); color: var(--white);
    white-space: nowrap;
  }

  .header-option--one .headline { left: 70px; top: 54px; color: var(--white); font-weight: 600; }
  .header-option--one .headline__top,
  .header-option--one .headline__main { text-shadow: 2px 3px 6px rgba(40,50,70,0.45); }
  .header-option--one .headline__top { font-size: 103px; letter-spacing: 0.28em; }
  .header-option--one .headline__main { font-size: 98px; letter-spacing: 0.05em; }
  .header-option--one .headline__tag {
    font-size: 54px; letter-spacing: 0.07em; padding: 0 4px 0 7px; margin-left: -5px;
  }

  .header-option--two .headline { left: 60px; top: 75px; color: var(--ink); font-weight: 500; }
  .header-option--two .headline__top { font-size: 97px; letter-spacing: 0.33em; }
  .header-option--two .headline__main { font-size: 100px; letter-spacing: 0.04em; margin-top: 2px; }
  .header-option--two .headline__tag {
    font-size: 48px; font-weight: 600; letter-spacing: 0.14em;
    padding: 1px 6px 1px 14px; margin-top: -4px; margin-left: -16px;
  }

  .option-label {
    position: absolute; left: 0; width: 1214px; text-align: center;
    font-weight: 600; letter-spacing: 0.02em; color: var(--ink); line-height: 1;
  }
  .option-label--one { top: 382px; font-size: 66px; }
  .option-label--two { top: 827px; font-size: 70px; }
</style>
</head>
<body>
<main class="board">
  <section class="header-option header-option--one">
    <div class="backdrop-photo" role="img" aria-label="Soft-focus city skyline in pale blue light"></div>
    <div class="portrait-photo" role="img" aria-label="Double-exposure businessman blended with a boardroom and city towers"></div>
    <h1 class="headline">
      <span class="headline__top">HOSTED</span>
      <span class="headline__main">DESKTOPS</span>
      <span class="headline__tag">FOR IT RESELLERS</span>
    </h1>
  </section>
  <p class="option-label option-label--one">HEADER 1</p>

  <section class="header-option header-option--two">
    <div class="crowd-photo" role="img" aria-label="Double-exposure business people walking through a blue city"></div>
    <h1 class="headline">
      <span class="headline__top">HOSTED</span>
      <span class="headline__main">DESKTOPS</span>
      <span class="headline__tag">FOR IT RESELLERS</span>
    </h1>
  </section>
  <p class="option-label option-label--two">HEADER 2</p>
</main>
</body>
</html>
```